Acupuncture Medspa needs a business card design

I need a business card design that looks professional, has a spa-like quality and can offer a promo on the back. Initial promo is "First session free". The tagline of NeedleNook is: Refresh, Restore, Rejuvenate.

NeedleNook is a membership-based acupuncture medspa that offers acupuncture, cupping, and herbal therapies. Members choose between the "Refresh" membership which is for stress relief, or "Restore" which is for treating health conditions, and lastly "Rejuvenate" which is for natural facial enhancement.

Industry/Entity Type

Health And Wellness

Contact Information for Business Card

Coral Haskins, MAC, L.Ac.
612-555-0193
www.needlenook-example.com

Font styles to use
Serif
Sans Serif

Colors

Designer to choose colors to be used in the design.

Requirements
Must have
• The project must have NeedleNook logo, promo on the back, and contact information
Nice to have
• I would like to see the colors of the logo used.

```html
<!DOCTYPE html>
<html lang="en">
<head>
<meta charset="utf-8">
<title>NeedleNook Business Card</title>
<link rel="stylesheet" href="https://fonts.googleapis.com/css2?family=Montserrat:wght@500;600;700&family=Nunito+Sans:wght@400&family=Cinzel:wght@600&display=swap">
<style>
  :root {
    --backdrop: #9a9a9a;
    --card: #ffffff;
    --teal: #0b8a80;
    --teal-soft: #4fb0a6;
    --teal-pale: #d7efec;
  }
  html, body {
    margin: 0;
    padding: 0;
    width: 1200px;
    height: 1000px;
    overflow: hidden;
    background: var(--backdrop);
  }
  .canvas {
    position: relative;
    width: 1200px;
    height: 1000px;
  }
  .card {
    position: absolute;
    width: 383px;
    height: 230px;
    background: var(--card);
    overflow: hidden;
    box-shadow: 0 2px 10px rgba(0,0,0,0.18);
  }
  .card--front { left: 157px; top: 385px; }
  .card--back  { left: 661px; top: 385px; }

  .brand-decoration {
    position: absolute;
    left: 0;
    top: 46px;
    width: 136px;
    height: 184px;
    background: linear-gradient(135deg, var(--teal-pale), #ffffff);
  }

  .contact {
    position: absolute;
    left: 172px;
    top: 123px;
    margin: 0;
    padding: 0;
    list-style: none;
    font-family: "Nunito Sans", sans-serif;
    font-size: 12px;
    line-height: 15px;
    color: var(--teal);
  }
  .contact li {
    display: flex;
    align-items: center;
    gap: 3px;
    white-space: nowrap;
  }
  .contact svg { width: 7px; height: 7px; flex: none; }

  .back-content {
    position: absolute;
    inset: 0;
    display: flex;
    flex-direction: column;
    align-items: center;
    padding-top: 102px;
  }
  .wordmark {
    display: flex;
    align-items: center;
    gap: 8px;
    font-family: "Montserrat", sans-serif;
    font-weight: 600;
    font-size: 26px;
    line-height: 1;
    color: var(--teal);
    letter-spacing: 0.5px;
  }
  .wordmark-dot {
    width: 10px;
    height: 10px;
    border-radius: 50%;
    background: var(--teal);
  }
  .tagline {
    margin-top: 7px;
    font-family: "Montserrat", sans-serif;
    font-weight: 700;
    font-size: 8.5px;
    letter-spacing: 0.3px;
    color: var(--teal);
  }
  .promo {
    margin-top: 24px;
    font-family: "Cinzel", serif;
    font-weight: 600;
    font-size: 12.5px;
    letter-spacing: 0.4px;
    color: var(--teal);
  }
</style>
</head>
<body>
<main class="canvas">
  <section class="card card--front">
    <div class="brand-decoration" role="img" aria-label="Brand emblem decoration area"></div>
    <ul class="contact">
      <li>
        <svg viewBox="0 0 10 10" aria-hidden="true"><path d="M5 0.5a3.3 3.3 0 0 0-3.3 3.3C1.7 6.3 5 9.5 5 9.5s3.3-3.2 3.3-5.7A3.3 3.3 0 0 0 5 .5zm0 4.6a1.3 1.3 0 1 1 0-2.6 1.3 1.3 0 0 1 0 2.6z" fill="currentColor"/></svg>
        Coral Haskins, MAC, L.Ac.
      </li>
      <li>
        <svg viewBox="0 0 10 10" aria-hidden="true"><path d="M2.3 0.8l1.5 1.9-.8 1.1c.6 1.3 1.5 2.2 2.8 2.8l1.1-.8 1.9 1.5-.9 1.6C4.6 8.7 1.3 5.4.7 1.7z" fill="currentColor"/></svg>
        612-555-0193
      </li>
      <li>
        <svg viewBox="0 0 10 10" aria-hidden="true"><circle cx="5" cy="5" r="4.2" fill="none" stroke="currentColor" stroke-width="1.2"/><circle cx="5" cy="5" r="1.6" fill="none" stroke="currentColor" stroke-width="1.1"/></svg>
        www.needlenook-example.com
      </li>
    </ul>
  </section>

  <section class="card card--back">
    <div class="back-content">
      <div class="wordmark"><span class="wordmark-dot" aria-hidden="true"></span>NeedleNook</div>
      <div class="tagline">REFRESH, RESTORE, REJUVENATE</div>
      <div class="promo">FIRST SESSION FREE</div>
    </div>
  </section>
</main>
</body>
</html>
```